Copper Vale Agency Website - Wordpress Web UPDATED BRIEF

FINAL LOGO UPLOADED - please look to this as reference for how we would like the site to look and feel.

We are a digital marketing agency - looking to have a new website built. We are looking for a simple one page feel of site that will allow us to grow it later. (Feel free to take some liberties with that if your imagination veers off) Must be very, playful, bold, sleek and easily integrate video. Wordpress only.

Overview:

Copper Vale is a creative constellation. We are built on what's great about the shared economy. With access to thousands of content creators, designers, technicians, writers, strategists and other creatives around the world, we are built differently than a traditional “brick and mortar” Marketing Agency. We provide the traditional services our clients have come to expect, without the “5X factor” of covering the overhead common in the old agency model. We believe even better work can be created in collaboration with our clients and by passing those savings back to them for their use. Our clients pay for our art, our work and our passion –not our furniture.

"Copper Vale, Let's Start Something"

Target Market(s)

companies looking for creative agency help, video production, creative consulting and coaching

Industry/Entity Type

Digital Marketing

Coding

Coded - Design and coding required

Number of Pages Required

1 page

Font styles to use
Sans Serif

Colors
3277b5
33a6d7
ec1f27

Requirements
Must have
• Wordpress design is a must. Looking for a one sheet homepage - with sections that are all on the main front page. We will have videos to embed, and should be able to have client logos and easy access to show a variety of our creative work.
• Please look to the logo for how we would like the site to feel.
• Please think "icon process flow" instead of blocks of text (which we used to have). Use the text to explain what the process flow should represent - don't actually copy paste the text but show it visually in icons.
Nice to have
• innovation around how we show video content. solid colors complementary to our palette and aesthetic.
Should not have
• Standard HTML coding

```html
<!DOCTYPE html>
<html lang="en">
<head>
<meta charset="utf-8">
<title>Copper Vale Agency</title>
<link href="https://fonts.googleapis.com/css2?family=Raleway:wght@500;600;700;800&family=Arimo:ital,wght@0,400;0,700;1,400&display=swap" rel="stylesheet">
<style>
:root{
  --blue:#3277b5;
  --blue-deep:#2d6db1;
  --blue-sky:#33a6d7;
  --blue-title:#3a8fd0;
  --red:#ec1f27;
  --page:#ebebeb;
  --ink:#2b2b2b;
  --muted:#7a7a7a;
  --white:#ffffff;
}
html,body{margin:0;padding:0;width:1200px;height:4345px;overflow:hidden;background:var(--page);}
.page{position:relative;width:1200px;height:4345px;overflow:hidden;background:var(--page);font-family:"Arimo",Arial,sans-serif;color:var(--ink);}
.backdrop{position:absolute;left:0;top:0;}
.abs{position:absolute;margin:0;}
.heading{font-family:"Raleway",Arial,sans-serif;font-weight:700;font-size:40px;line-height:48px;letter-spacing:.5px;}
.heading--light{color:var(--blue-title);}
.heading--deep{color:var(--blue-deep);}
.center{left:0;width:1200px;text-align:center;}
.lead{font-size:15px;line-height:36px;color:#333;}
.btn{display:flex;align-items:center;justify-content:center;gap:7px;background:var(--red);color:var(--white);font-family:"Raleway",Arial,sans-serif;font-weight:700;font-size:16px;border-radius:27px;text-decoration:none;}
.btn svg{width:16px;height:16px;}

/* header */
.brand{position:absolute;left:138px;top:38px;display:flex;align-items:center;gap:10px;}
.brand__mark{width:54px;height:54px;border-radius:50%;background:var(--blue-deep);}
.brand__name{font-family:"Raleway",Arial,sans-serif;font-weight:800;font-size:20px;color:#1d1d1d;}
.nav{position:absolute;right:91px;top:48px;display:flex;gap:34px;font-family:"Raleway",Arial,sans-serif;font-weight:600;font-size:17px;}
.nav a{color:var(--white);text-decoration:none;}
.hero__title{right:90px;top:190px;font-family:"Raleway",Arial,sans-serif;font-weight:600;font-size:42px;line-height:50px;color:var(--white);}
.hero__text{right:90px;top:256px;width:520px;text-align:right;font-size:16px;line-height:32px;color:var(--white);font-weight:700;}
.hero__btn{left:906px;top:338px;width:204px;height:52px;}
.dots{left:1040px;top:416px;display:flex;gap:11px;align-items:center;}
.dots span{width:10px;height:10px;border-radius:50%;background:var(--white);}
.dots .on{width:12px;height:12px;background:transparent;border:3px solid var(--white);box-sizing:border-box;position:relative;}
.video{left:89px;top:471px;width:633px;height:381px;box-sizing:border-box;border:4px solid var(--white);background:linear-gradient(135deg,#2d6db1,#3b8fd6);box-shadow:0 2px 6px rgba(0,0,0,.15);}
.video__play{position:absolute;left:50%;top:50%;width:70px;height:50px;margin:-25px 0 0 -35px;background:var(--red);border-radius:12px;}
.video__play::after{content:"";position:absolute;left:28px;top:14px;border-left:18px solid var(--white);border-top:11px solid transparent;border-bottom:11px solid transparent;}

/* clients */
.clients__title{top:1071px;}
.clients__text{left:150px;width:900px;top:1130px;text-align:center;}
.logo-grid{left:105px;top:1230px;width:991px;display:grid;grid-template-columns:repeat(5,185px);grid-auto-rows:112px;column-gap:16.5px;row-gap:13px;}
.logo-cell{background:var(--white);border:1px solid #cfcfcf;display:flex;align-items:center;justify-content:center;gap:8px;font-family:"Raleway",Arial,sans-serif;font-weight:700;font-size:21px;}
.logo-cell--soft{background:#f4f4f4;}
.logo-cell i{width:14px;height:14px;display:block;}

/* about */
.device{border-radius:10px 10px 4px 4px;}
.about__device{left:42px;top:1659px;width:515px;height:294px;background:linear-gradient(180deg,#262626 0 4%,#f3f4f7 4% 93%,#b9bcc2 93%);}
.about__title{left:574px;top:1681px;}
.about__text{left:574px;top:1742px;width:535px;text-align:justify;font-size:15px;line-height:35.7px;color:#333;}
.about__btn{left:574px;top:1936px;width:202px;height:52px;}

/* services */
.services__title{top:2136px;}
.services__text{left:95px;width:1010px;top:2194px;text-align:center;font-size:15px;line-height:32px;color:#333;}
.service{position:absolute;width:210px;height:210px;border-radius:50%;background:var(--white);border:2px solid #dcdcdc;box-sizing:border-box;text-align:center;box-shadow:0 3px 10px rgba(0,0,0,.06);}
.service--active{background:var(--blue-deep);border-color:var(--blue-deep);color:var(--white);}
.service svg{position:absolute;left:75px;top:22px;width:60px;height:60px;}
.service h3{position:absolute;left:0;right:0;top:98px;margin:0;font-family:"Raleway",Arial,sans-serif;font-size:15px;font-weight:700;letter-spacing:.5px;}
.service p{position:absolute;left:20px;right:20px;top:124px;margin:0;font-size:13px;line-height:20px;color:#555;}
.service--active p{color:var(--white);}
.emblem{left:402px;top:2451px;width:369px;height:360px;border-radius:50%;background:radial-gradient(circle at 40% 35%,#4a9be0,#2d6db1 70%);}
.emblem__name{left:0;width:1200px;text-align:center;top:2818px;font-family:"Raleway",Arial,sans-serif;font-weight:800;font-size:30px;color:#1d1d1d;letter-spacing:1px;}

/* testimonials */
.reviews__title{top:2944px;font-weight:600;font-size:38px;}
.review{position:absolute;top:3043px;width:313px;height:174px;background:var(--white);border-radius:6px;box-shadow:0 2px 10px rgba(0,0,0,.1);}
.review__avatar{position:absolute;left:24px;top:24px;width:44px;height:44px;border-radius:50%;background:#d5d5d5;}
.review__avatar::after{content:"";position:absolute;left:15px;top:9px;width:14px;height:14px;border-radius:50%;background:var(--white);box-shadow:0 16px 0 4px var(--white);}
.review__name{position:absolute;left:88px;top:25px;margin:0;font-size:16px;color:#222;}
.review__role{position:absolute;left:88px;top:47px;margin:0;font-size:13px;font-style:italic;color:var(--muted);}
.review__text{position:absolute;left:22px;right:20px;top:88px;margin:0;font-size:13px;line-height:22px;font-style:italic;color:#555;}
.arrow{position:absolute;top:3121px;width:22px;height:28px;}

/* work */
.work__title{left:89px;top:3445px;}
.work__text{left:89px;top:3505px;width:536px;text-align:justify;font-size:15px;line-height:35.7px;color:#333;}
.work__btn{left:89px;top:3698px;width:205px;height:53px;}
.work__device{left:641px;top:3410px;width:519px;height:295px;background:linear-gradient(180deg,#262626 0 4%,#f3f4f7 4% 93%,#b9bcc2 93%);}

/* footer */
.foot__title{font-family:"Raleway",Arial,sans-serif;font-weight:600;font-size:26px;line-height:32px;color:#222;}
.contact{left:89px;top:4058px;}
.contact dt{font-size:14px;color:#444;margin-top:12px;}
.contact dd{margin:6px 0 0;font-size:13px;color:var(--muted);}
.links{left:338px;top:4058px;}
.links ul{list-style:none;margin:14px 0 0;padding:0;}
.links li{font-size:13px;line-height:27px;color:#555;}
.newsletter{left:670px;top:4054px;width:440px;color:var(--white);}
.newsletter .foot__title{color:var(--white);font-size:32px;line-height:40px;}
.newsletter p{margin:10px 0 0;font-size:14px;line-height:27px;}
.subscribe{position:absolute;left:0;top:137px;width:439px;height:60px;border-radius:30px;background:var(--white);box-sizing:border-box;}
.subscribe span{position:absolute;left:38px;top:21px;font-size:14px;color:#666;}
.subscribe b{position:absolute;right:4px;top:5px;width:140px;height:50px;border-radius:25px;background:var(--red);color:var(--white);font-weight:400;font-size:17px;display:flex;align-items:center;justify-content:center;}
.copyright{left:738px;top:4300px;font-size:12px;color:var(--white);}
</style>
</head>
<body>
<div class="page">

<svg class="backdrop" width="1200" height="4345" viewBox="0 0 1200 4345" aria-hidden="true">
  <defs>
    <linearGradient id="heroBlue" x1="0" y1="0" x2="1" y2="1">
      <stop offset="0" stop-color="#2d6db1"/><stop offset="1" stop-color="#2f86cc"/>
    </linearGradient>
    <linearGradient id="waveBlue" x1="0" y1="0" x2="1" y2="1">
      <stop offset="0" stop-color="#2d6db1"/><stop offset="1" stop-color="#33a0d8"/>
    </linearGradient>
  </defs>
  <!-- hero shape -->
  <path d="M228 0 C236 200 420 340 700 560 C880 700 1060 840 1200 880 V0 Z" fill="url(#heroBlue)"/>
  <!-- about wave -->
  <path d="M0 1628 C50 1618 90 1546 170 1546 C250 1546 280 1640 380 1660 L560 1700 L560 1950 C420 1962 300 1980 180 2000 C100 2012 40 2018 0 2018 Z" fill="url(#waveBlue)"/>
  <path d="M0 1620 C50 1610 92 1536 172 1536 C252 1536 285 1632 385 1652" fill="none" stroke="#ffffff" stroke-width="6"/>
  <!-- service arcs -->
  <g fill="none" stroke="#3277b5" stroke-width="1.5" stroke-dasharray="5 5">
    <path d="M440 2305 Q600 2260 770 2305"/>
    <path d="M275 2475 Q222 2550 208 2612"/>
    <path d="M935 2475 Q988 2550 1000 2612"/>
  </g>
  <!-- soft band -->
  <path d="M0 2900 C300 2860 800 2880 1200 2830 V2900 H0 Z" fill="#f1f1f1"/>
  <!-- work wave -->
  <path d="M760 3455 C820 3400 880 3358 960 3362 C1060 3368 1120 3398 1200 3396 V3870 C1100 3862 1000 3800 900 3740 L700 3700 Z" fill="url(#waveBlue)"/>
  <path d="M800 3430 C860 3380 900 3350 960 3352 C1060 3358 1120 3388 1200 3386" fill="none" stroke="#ffffff" stroke-width="6"/>
  <!-- footer -->
  <rect x="0" y="4170" width="1200" height="175" fill="#ffffff"/>
  <path d="M439 4345 C520 4200 600 4050 760 3990 C860 3942 940 3918 1060 3928 C1130 3934 1170 3944 1200 3950 V4345 Z" fill="url(#heroBlue)"/>
</svg>

<header>
  <div class="brand"><span class="brand__mark"></span><span class="brand__name">COPPER VALE</span></div>
  <nav class="nav">
    <a href="#">Home</a><a href="#">Clients</a><a href="#">About</a><a href="#">Services</a><a href="#">Testimonials</a><a href="#">Creative Work</a><a href="#">Contact</a>
  </nav>
</header>

<section class="hero">
  <h1 class="abs hero__title">WELCOME TO COPPER VALE</h1>
  <p class="abs hero__text">Sed ut perspiciatis unde omnis iste natus error sit accusantium doloremque laudantium</p>
  <a class="abs btn hero__btn" href="#">READ MORE <svg viewBox="0 0 16 16"><circle cx="8" cy="8" r="6.5" fill="none" stroke="#fff" stroke-width="1.6"/><path d="M5 8h6M8.5 5.5 11 8l-2.5 2.5" fill="none" stroke="#fff" stroke-width="1.6"/></svg></a>
  <div class="abs dots"><span class="on"></span><span></span><span></span><span></span></div>
  <div class="abs video" role="img" aria-label="Video player showing the Copper Vale mascot intro"><span class="video__play"></span></div>
</section>

<section class="clients">
  <h2 class="abs heading heading--light center clients__title">OUR CLIENTS</h2>
  <p class="abs lead clients__text">Sed ut perspiciatis unde omnis iste natus error sit voluptatem accusantium doloremque laudantium, totam rem aperiam, eaque ipsa quae ab illo inventore veritatis et quasi architecto beatae vitae dicta sunt explicabo.</p>
  <div class="abs logo-grid">
    <div class="logo-cell" style="color:#555">Marlow Fields</div>
    <div class="logo-cell" style="color:#222">Forgeworks</div>
    <div class="logo-cell" style="color:#222">Tall Mock</div>
    <div class="logo-cell logo-cell--soft" style="color:#222">Pivotly</div>
    <div class="logo-cell" style="color:#222">Quartile</div>
    <div class="logo-cell" style="color:#1f6b3a">Firmsite</div>
    <div class="logo-cell" style="color:#333">Velvet Flair</div>
    <div class="logo-cell" style="color:#e0452b">Sprout Pulse</div>
    <div class="logo-cell logo-cell--soft" style="color:#b8912f"><i style="background:#b8912f;border-radius:50%"></i>Coinway</div>
    <div class="logo-cell" style="color:#333">Fernhouse</div>
  </div>
</section>

<section class="about">
  <div class="abs device about__device" role="img" aria-label="Laptop illustration with a man presenting charts on screen"></div>
  <h2 class="abs heading heading--deep about__title">ABOUT US</h2>
  <p class="abs about__text">Copper Vale is a creative constellation. We are built on what's great about the shared economy. With access to thousands of content creators, designers, technicians, writers, strategists and other creatives around the world, we are built differently than a traditional “brick and mortar” Marketing Agency.</p>
  <a class="abs btn about__btn" href="#">READ MORE <svg viewBox="0 0 16 16"><circle cx="8" cy="8" r="6.5" fill="none" stroke="#fff" stroke-width="1.6"/><path d="M5 8h6M8.5 5.5 11 8l-2.5 2.5" fill="none" stroke="#fff" stroke-width="1.6"/></svg></a>
</section>

<section class="services">
  <h2 class="abs heading heading--light center services__title">OUR SERVICES</h2>
  <p class="abs services__text">Sed ut perspiciatis unde omnis iste natus error sit voluptatem accusantium doloremque laudantium, totam rem aperiam, eaque ipsa quae ab illo inventore veritatis et quasi architecto beatae vitae dicta sunt explicabo.</p>

  <div class="service service--active" style="left:243px;top:2284px">
    <svg viewBox="0 0 60 60" fill="none" stroke="#fff" stroke-width="2"><path d="M30 8a14 14 0 0 0-8 25v7h16v-7a14 14 0 0 0-8-25z"/><path d="M24 45h12M26 50h8M30 16v10l6 4"/></svg>
    <h3>STRATEGY</h3><p>Lorem ipsum dolor sit, consect adipiscing.</p>
  </div>
  <div class="service" style="left:756px;top:2285px">
    <svg viewBox="0 0 60 60" fill="none" stroke="#3277b5" stroke-width="2"><circle cx="30" cy="11" r="6"/><path d="M20 28c0-6 4-9 10-9s10 3 10 9"/><rect x="16" y="30" width="28" height="6"/><path d="M20 36v18M40 36v18M24 54h12"/><circle cx="44" cy="46" r="6"/></svg>
    <h3>COACHING</h3><p>Lorem ipsum dolor sit, consect adipiscing.</p>
  </div>
  <div class="service" style="left:91px;top:2613px">
    <svg viewBox="0 0 60 60" fill="none" stroke="#3277b5" stroke-width="2"><circle cx="30" cy="32" r="18"/><ellipse cx="30" cy="32" rx="8" ry="18"/><path d="M12 32h36M15 23h30M15 41h30M22 8l8-4 8 4"/></svg>
    <h3>DISCOVERY</h3><p>Lorem ipsum dolor sit, consect adipiscing.</p>
  </div>
  <div class="service" style="left:899px;top:2613px">
    <svg viewBox="0 0 60 60" fill="none" stroke="#3277b5" stroke-width="2"><path d="M12 6h26l8 8v40H12z"/><path d="M38 6v8h8M18 20h18M18 27h14M18 34h10M18 41h8"/><path d="M30 46l4-8 16-16 4 4-16 16z"/></svg>
    <h3>CONTENT</h3><p>Lorem ipsum dolor sit, consect adipiscing.</p>
  </div>

  <div class="abs emblem" role="img" aria-label="Copper Vale mascot emblem"></div>
  <p class="abs emblem__name">COPPER VALE</p>
</section>

<section class="reviews">
  <h2 class="abs heading heading--light center reviews__title">What Our Clients Say’s</h2>
  <svg class="arrow" style="left:34px" viewBox="0 0 22 28"><path d="M16 4 6 14l10 10" fill="none" stroke="#3277b5" stroke-width="4"/></svg>
  <article class="review" style="left:89px">
    <span class="review__avatar"></span><h4 class="review__name">Lena Morrow</h4><p class="review__role">Lorem ipsum dolor sit</p>
    <p class="review__text">Lorem ipsum dolor sit amet, consectetur adipiscing elit, sed do modd tempor idunt ut labore et dolore magna aliqua</p>
  </article>
  <article class="review" style="left:444px">
    <span class="review__avatar"></span><h4 class="review__name">Derek Vance</h4><p class="review__role">Lorem ipsum dolor sit</p>
    <p class="review__text">Lorem ipsum dolor sit amet, consectetur adipiscing elit, sed do modd tempor idunt ut labore et dolore magna aliqua</p>
  </article>
  <article class="review" style="left:797px">
    <span class="review__avatar"></span><h4 class="review__name">Hana Sato</h4><p class="review__role">Lorem ipsum dolor sit</p>
    <p class="review__text">Lorem ipsum dolor sit amet, consectetur adipiscing elit, sed do modd tempor idunt ut labore et dolore magna aliqua</p>
  </article>
  <svg class="arrow" style="left:1146px" viewBox="0 0 22 28"><path d="M6 4l10 10L6 24" fill="none" stroke="#3277b5" stroke-width="4"/></svg>
</section>

<section class="work">
  <h2 class="abs heading heading--deep work__title">OUR CREATIVE WORK</h2>
  <p class="abs work__text">Copper Vale is a creative constellation. We are built on what's great about the shared economy. With access to thousands of content creators, designers, technicians, writers, strategists and other creatives around the world, we are built differently than a traditional “brick and mortar” Marketing Agency.</p>
  <a class="abs btn work__btn" href="#">VIEW MORE <svg viewBox="0 0 16 16"><circle cx="8" cy="8" r="6.5" fill="none" stroke="#fff" stroke-width="1.6"/><path d="M5 8h6M8.5 5.5 11 8l-2.5 2.5" fill="none" stroke="#fff" stroke-width="1.6"/></svg></a>
  <div class="abs device work__device" role="img" aria-label="Laptop illustration with a woman arranging design boards"></div>
</section>

<footer>
  <div class="abs contact">
    <h3 class="foot__title" style="margin:0">Contact Us</h3>
    <dl style="margin:8px 0 0">
      <dt>Email address</dt><dd>hello@coppervaleagency.com</dd>
      <dt style="margin-top:18px">Call us</dt><dd>+1 555 014 2290</dd>
    </dl>
  </div>
  <div class="abs links">
    <h3 class="foot__title" style="margin:0">Links</h3>
    <ul><li>Home</li><li>Clients</li><li>About</li><li>Services</li><li>Testimonials</li><li>Creative Work</li><li>Contact</li></ul>
  </div>
  <div class="abs newsletter">
    <h3 class="foot__title" style="margin:0">Newsletter</h3>
    <p>Lorem ipsum dolor sit amet, consectetur adipiscing elit,<br>sed do eiusmod tempor incididunt ut</p>
    <div class="subscribe"><span>Enter Your Email Address</span><b>Sign Up</b></div>
  </div>
  <p class="abs copyright">© Copyrights 2019. The Company name.All Rights Reserved</p>
</footer>

</div>
</body>
</html>
```